Landscape Contractor in need of New Web Design

HELP.. Please Help!!!!. Our current website is old, outdated, ugly... and well nothing like us.... so we are looking for someone to help build a new website that fits our company direction. We are a landscape company with multiple locations in order to meet the needs of our clients and their projects throughout the midwest. When most people think of landscaping, they think of mowing grandmas yard, but that is NOT even remotely close to what we do. We are 100% a commercial landscape company meaning we complete landscape and irrigation services for large scale commercial projects. We are looking for a website to showcase our commercial talents and awesome team of people.
Updates

Address of current website is www.brookvaleyardworks.com

```html
<!DOCTYPE html>
<html lang="en">
<head>
<meta charset="utf-8">
<title>Brookvale Yardworks – Landscaping Maintenance Services</title>
<link rel="stylesheet" href="https://fonts.googleapis.com/css2?family=Montserrat:wght@300;400;500;600;700;800;900&display=swap">
<style>
:root{
  --lime:#aef200;
  --lime-dark:#8fcc00;
  --green:#3f8a1c;
  --green-deep:#2f6c12;
  --mint:#e9f4e4;
  --ink:#111111;
  --text:#3d3d3d;
  --muted:#6b6b6b;
  --black:#0e0e0e;
  --white:#ffffff;
}
*{box-sizing:border-box;margin:0;padding:0}
html,body{width:1200px;height:4285px;overflow:hidden}
body{position:relative;background:var(--white);font-family:"Montserrat",sans-serif;color:var(--text)}
.abs{position:absolute}

/* header */
.brand{left:173px;top:6px;display:flex;align-items:center;gap:10px;height:72px}
.brand-dot{width:30px;height:30px;border-radius:50%;background:var(--lime)}
.brand-name{font-weight:800;font-size:17px;color:var(--ink);line-height:1.1;width:120px}
.contact-item{top:20px;display:flex;gap:10px;font-size:11px;line-height:14px}
.contact-item svg{margin-top:6px}
.contact-item .label{color:var(--muted)}
.contact-item .value{color:var(--green);font-weight:700}
.phone{left:768px}.hours{left:916px}

.nav{left:173px;top:85px;width:854px;height:53px;background:var(--black);display:flex;align-items:center;z-index:3}
.nav a{color:var(--white);text-decoration:none;font-size:11px;font-weight:700;letter-spacing:.4px;margin-left:22px}
.nav a.active{color:var(--lime);margin-left:24px}
.nav .quote{position:absolute;right:0;top:0;height:53px;width:140px;background:var(--lime);color:var(--ink);display:flex;align-items:center;justify-content:center;clip-path:polygon(18% 0,100% 0,100% 100%,0 100%);padding-left:20px;margin:0}

/* hero */
.hero{left:0;top:103px;width:1200px;height:496px;background:linear-gradient(100deg,#1f3a14 0%,#2f5a1c 35%,#4f8030 62%,#3d6a24 80%,#2a4a1a 100%)}
.hero-eyebrow{left:173px;top:208px;color:var(--white);font-size:11px;font-weight:700;letter-spacing:.5px}
.hero-title{left:173px;top:222px;color:var(--white);font-size:54px;font-weight:800;line-height:52px;letter-spacing:1px}
.hero-sub{left:173px;top:384px;color:var(--white);font-size:13px;font-weight:600}
.btn-lime{left:173px;top:443px;width:152px;height:35px;background:var(--lime);border-radius:4px;color:var(--ink);font-size:10px;font-weight:800;display:flex;align-items:center;justify-content:center;letter-spacing:.4px}

/* about */
.about-bg{left:474px;top:602px;width:726px;height:663px;background:var(--mint)}
.about-photo{left:173px;top:687px;width:418px;height:483px;background:linear-gradient(135deg,#5d8a2f 0%,#8aa85a 45%,#6f7a55 100%);box-shadow:0 18px 30px rgba(0,0,0,.18)}
.section-h{color:var(--ink);font-weight:800;font-size:39px}
.about-title{left:626px;top:770px}
.rule{height:3px;width:54px;background:var(--green)}
.about-rule{left:626px;top:836px}
.about-text{left:626px;top:858px;width:390px;font-size:12.5px;line-height:18px;color:var(--muted)}
.feature{top:942px;width:114px;height:126px;background:var(--white);display:flex;flex-direction:column;align-items:center;justify-content:flex-end;padding-bottom:16px;font-size:13px;font-weight:600;color:var(--ink);gap:14px}
.feature svg{display:block}

/* services */
.services-title{left:0;width:1200px;top:1378px;text-align:center}
.services-rule{left:561px;top:1447px;width:78px}
.svc{width:418px;height:113px;background:var(--white);box-shadow:0 3px 18px rgba(0,0,0,.07);padding:24px 20px 0 110px}
.svc svg{position:absolute;left:12px;top:26px}
.svc h3{font-size:16px;font-weight:500;color:var(--green-deep);margin-bottom:6px;margin-left:-2px}
.svc p{font-size:11px;line-height:17px;color:var(--muted)}
.svc.right{padding-left:98px}
.btn-outline{left:541px;top:1804px;width:116px;height:35px;border:2px solid var(--lime);font-size:12px;font-weight:600;color:var(--ink);display:flex;align-items:center;justify-content:center}

/* we are */
.weare-band{left:0;top:1970px;width:614px;height:391px;background:var(--mint)}
.weare-title{left:196px;top:2036px;font-size:39px}
.weare-rule{left:196px;top:2107px}
.weare-text{left:196px;top:2133px;width:345px;font-size:19px;font-weight:300;line-height:26.5px;color:var(--ink)}
.arrow-btn{top:2270px;width:33px;height:31px;display:flex;align-items:center;justify-content:center}
.arrow-prev{left:196px;background:var(--white);border:1px solid #bbb}
.arrow-next{left:236px;background:#6ea531}
.sports-photo{left:614px;top:1935px;width:391px;height:453px;background:linear-gradient(160deg,#1f3d12 0%,#3f7a1f 40%,#5fa42c 100%)}
.sports-frame{left:671px;top:2005px;width:279px;height:313px;border:2px solid var(--lime)}
.sports-card{left:687px;top:2025px;width:247px;height:276px;background:var(--lime);display:flex;align-items:center;justify-content:center;font-size:20px;font-weight:500;color:var(--ink)}
.gallery{top:2411px;width:391px;height:453px}
.gallery-path{left:200px;background:linear-gradient(160deg,#4e8f2a 0%,#6ba83a 50%,#3f7a22 100%)}
.gallery-sign{left:616px;background:linear-gradient(180deg,#6f9bc9 0%,#9b9070 35%,#8fc34a 60%,#4c7f22 100%)}

/* testimonials */
.eyebrow{left:0;width:1200px;top:2991px;text-align:center;font-size:15px;font-weight:700;letter-spacing:4px;color:var(--ink)}
.testi-title{left:0;width:1200px;top:3013px;text-align:center}
.testi-rule{left:561px;top:3081px;width:78px}
.testi{top:3157px;width:268px;height:213px;background:var(--mint);text-align:center;padding:54px 20px 0}
.testi p{font-size:11px;line-height:21.5px;color:var(--text)}
.testi .name{font-size:11px;font-weight:700;color:var(--green-deep);margin-top:8px}
.testi .role{font-size:11px;margin-top:4px;color:var(--text)}
.avatar{width:54px;height:54px;border-radius:50%;background:linear-gradient(180deg,#c9c9c9,#7d7d7d);border:3px solid var(--white);top:3128px}
.qbadge{width:54px;height:54px;border-radius:50%;background:var(--white);top:3343px;display:flex;align-items:center;justify-content:center;box-shadow:0 2px 6px rgba(0,0,0,.06)}

/* quote */
.quote-bg{left:0;top:3493px;width:1200px;height:526px;background:linear-gradient(110deg,#1e3a12 0%,#3c6e20 40%,#254a16 100%)}
.quote-box{left:173px;top:3543px;width:468px;height:431px;background:var(--lime)}
.quote-title{left:198px;top:3592px;font-size:25px;font-weight:800;line-height:32px;color:var(--ink)}
.quote-photo{left:597px;top:3593px;width:445px;height:334px;background:linear-gradient(170deg,#6d8d4a 0%,#4e7a2b 45%,#8a7a6a 65%,#3f6b1e 100%)}
.field{background:var(--white);border-radius:5px;font-size:9px;color:#555;padding:11px 10px}
.f-first{left:198px;top:3698px;width:183px;height:35px}
.f-email{left:391px;top:3698px;width:183px;height:35px}
.f-select{left:198px;top:3744px;width:376px;height:33px;padding-top:10px}
.f-select svg{position:absolute;right:12px;top:13px}
.f-msg{left:198px;top:3791px;width:376px;height:75px}
.btn-black{left:198px;top:3882px;width:151px;height:37px;background:var(--black);color:var(--white);border-radius:5px;font-size:10px;font-weight:700;display:flex;align-items:center;justify-content:center}

/* footer */
.foot-h{top:4077px;font-size:13px;font-weight:700;color:var(--ink)}
.foot-col{top:4104px;font-size:9.5px;line-height:14.5px;color:var(--muted)}
.foot-about{width:180px;font-size:8.5px;line-height:12.5px}
.foot-links div{line-height:20px}
.social{left:910px;top:4104px;display:flex;gap:6px}
.social span{width:25px;height:25px;border-radius:50%;background:var(--green);display:block}
.social span+span{background:#4a4a4a}
.foot-line{left:173px;top:4227px;width:854px;height:1px;background:#e3e3e3}
.copy{left:173px;top:4252px;font-size:9.5px;color:var(--muted)}
.legal{right:173px;top:4252px;font-size:9.5px;color:var(--muted)}
</style>
</head>
<body>

<!-- header -->
<div class="abs brand"><span class="brand-dot"></span><span class="brand-name">Brookvale Yardworks</span></div>
<div class="abs contact-item phone">
  <svg width="18" height="18" viewBox="0 0 24 24" fill="none" stroke="#3f8a1c" stroke-width="1.8"><path d="M5 3h4l2 5-2.5 1.5a11 11 0 0 0 6 6L16 13l5 2v4a2 2 0 0 1-2 2A17 17 0 0 1 3 5a2 2 0 0 1 2-2z"/></svg>
  <div><div class="label">Phone Number</div><div class="value">(913) 555-0148</div><div class="value">(785) 555-0193</div></div>
</div>
<div class="abs contact-item hours">
  <svg width="18" height="18" viewBox="0 0 24 24" fill="none" stroke="#3f8a1c" stroke-width="1.8"><circle cx="12" cy="12" r="9"/><path d="M12 7v5l3 2"/></svg>
  <div><div class="label">Business Hours</div><div class="value">8am - 5pm :</div><div class="value">Mon - Fri</div></div>
</div>

<!-- hero -->
<div class="abs hero" role="img" aria-label="Gardener holding a crate of flowering plants on a green lawn in front of a house"></div>
<nav class="abs nav">
  <a class="active">HOME</a><a>DIVISIONS</a><a>SERVICES</a><a>ABOUT US</a><a>GALLERY CONTACT</a>
  <a class="quote">GET A QUOTE</a>
</nav>
<div class="abs hero-eyebrow">WELCOME TO BROOKVALE YARDWORKS</div>
<h1 class="abs hero-title">Landscaping<br>Maintenance<br>Services</h1>
<div class="abs hero-sub">With the goal of craftinga Purposeful Landscape</div>
<div class="abs btn-lime">LEARN MORE</div>

<!-- about -->
<div class="abs about-bg"></div>
<div class="abs about-photo" role="img" aria-label="Smiling gardener in gloves pruning a plant"></div>
<h2 class="abs section-h about-title">Brookvale Yardworks</h2>
<div class="abs rule about-rule"></div>
<p class="abs about-text">Our company's dedication to innovative design projects created some of the most distinguished landscape projects throughout Kansas, Missouri, and Oklahoma.</p>
<div class="abs feature" style="left:626px">
  <svg width="64" height="50" viewBox="0 0 64 50" fill="none" stroke="#3f8a1c" stroke-width="2"><path d="M32 4l-12 42M32 4l12 42M24 30h16"/><circle cx="32" cy="6" r="3"/><path d="M8 46c0-14 4-24 4-24s4 10 4 24M48 46c0-14 4-24 4-24s4 10 4 24"/></svg>Landscape</div>
<div class="abs feature" style="left:754px">
  <svg width="64" height="50" viewBox="0 0 64 50" fill="none" stroke="#3f8a1c" stroke-width="2"><path d="M32 6c-8 6-8 18 0 24 8-6 8-18 0-24zM32 30v10"/><path d="M8 20l8 16 10 8M56 20l-8 16-10 8"/></svg>Hardscape</div>
<div class="abs feature" style="left:880px">
  <svg width="64" height="50" viewBox="0 0 64 50" fill="none" stroke="#3f8a1c" stroke-width="2"><path d="M32 42V14M32 22l-12-8M32 22l12-8M32 30l-14-4M32 30l14-4M14 44h36"/><path d="M24 44l-4-6M40 44l4-6"/></svg>Irrigation</div>

<!-- services -->
<h2 class="abs section-h services-title">Our Services</h2>
<div class="abs rule services-rule"></div>
<div class="abs svc" style="left:173px;top:1494px">
  <svg width="62" height="60" viewBox="0 0 62 60" fill="none" stroke="#9ad400" stroke-width="2"><path d="M6 56V30l6-6 6 6v26M24 56V30l6-6 6 6v26M42 56V30l6-6 6 6v26M2 40h58M2 50h58"/></svg>
  <h3>Maintenance</h3><p>Lorem ipsum dolor sit amet, conset etur sadipscing elitr, sed diam noket numy eirmod tempor</p></div>
<div class="abs svc right" style="left:609px;top:1494px">
  <svg width="62" height="64" viewBox="0 0 62 64" fill="none" stroke="#9ad400" stroke-width="2"><rect x="20" y="20" width="32" height="40" rx="3"/><circle cx="36" cy="42" r="7"/><path d="M28 20v-8h16v8M14 8h10M14 8v30"/></svg>
  <h3>Chemical Applications &amp; Fertilization</h3><p>Lorem ipsum dolor sit amet, conset etur sadipscing elitr, sed diam noket numy eirmod tempor</p></div>
<div class="abs svc" style="left:173px;top:1629px">
  <svg width="80" height="56" viewBox="0 0 80 56" fill="none" stroke="#9ad400" stroke-width="2"><circle cx="14" cy="38" r="10"/><circle cx="14" cy="38" r="4"/><path d="M14 28h56v20H14M24 14h48v14M24 14a8 8 0 0 0 0 14"/></svg>
  <h3>Turf Management</h3><p>Lorem ipsum dolor sit amet, conset etur sadipscing elitr, sed diam noket numy eirmod tempor</p></div>
<div class="abs svc right" style="left:609px;top:1629px">
  <svg width="62" height="60" viewBox="0 0 62 60" fill="none" stroke="#9ad400" stroke-width="2"><ellipse cx="30" cy="12" rx="10" ry="5"/><ellipse cx="30" cy="26" rx="16" ry="6"/><ellipse cx="30" cy="42" rx="22" ry="8"/><path d="M48 52c4-6 8-8 12-8"/></svg>
  <h3>Hardscaping</h3><p>Lorem ipsum dolor sit amet, conset etur sadipscing elitr, sed diam noket numy eirmod tempor</p></div>
<div class="abs btn-outline">All Services</div>

<!-- we are -->
<div class="abs weare-band"></div>
<h2 class="abs section-h weare-title">We Are</h2>
<div class="abs rule weare-rule"></div>
<p class="abs weare-text">Brookvale Yardworks is a full service lawn and landscape contractor providing design, installation, and maintenance services.</p>
<div class="abs arrow-btn arrow-prev"><svg width="8" height="10" viewBox="0 0 8 10" fill="none" stroke="#111" stroke-width="2"><path d="M6 1L2 5l4 4"/></svg></div>
<div class="abs arrow-btn arrow-next"><svg width="8" height="10" viewBox="0 0 8 10" fill="none" stroke="#fff" stroke-width="2"><path d="M2 1l4 4-4 4"/></svg></div>
<div class="abs sports-photo" role="img" aria-label="Mower striping a sports field"></div>
<div class="abs sports-frame"></div>
<div class="abs sports-card">SPORTS FIELDS</div>
<div class="abs gallery gallery-path" role="img" aria-label="Curving stepping-stone path across a lawn"></div>
<div class="abs gallery gallery-sign" role="img" aria-label="Stone information center sign surrounded by planted beds"></div>

<!-- testimonials -->
<div class="abs eyebrow">CLIENT TESTIMONIALS</div>
<h2 class="abs section-h testi-title">What our clients say</h2>
<div class="abs rule testi-rule"></div>

<div class="abs testi" style="left:175px"><p>Called Fernway for service and tech arrived on 24 hrs later and performed a repair for a reasonable price.</p><div class="name">Marcus Hale</div><div class="role">Tincidunt</div></div>
<div class="abs testi" style="left:466px"><p>Fernway and crew did a fantastic install of a Rainline WiFi sprinkler system. The neatest crew we have ever at home....</p><div class="name">Dana Whitfield</div><div class="role">Nulla nec</div></div>
<div class="abs testi" style="left:755px"><p>Called Fernway for service and tech arrived on 24 hrs later and performed a repair for a reasonable price.</p><div class="name">Victor Salas</div><div class="role">Consectetuir</div></div>
<div class="abs avatar" style="left:282px" role="img" aria-label="Client portrait"></div>
<div class="abs avatar" style="left:573px" role="img" aria-label="Client portrait"></div>
<div class="abs avatar" style="left:862px" role="img" aria-label="Client portrait"></div>
<div class="abs qbadge" style="left:282px"><svg width="26" height="20" viewBox="0 0 26 20" fill="#3f8a1c"><path d="M0 20V11C0 4 4 0 10 0v4c-3 0-5 2-5 6h5v10zM14 20V11c0-7 4-11 10-11v4c-3 0-5 2-5 6h5v10z"/></svg></div>
<div class="abs qbadge" style="left:573px"><svg width="26" height="20" viewBox="0 0 26 20" fill="#3f8a1c"><path d="M0 20V11C0 4 4 0 10 0v4c-3 0-5 2-5 6h5v10zM14 20V11c0-7 4-11 10-11v4c-3 0-5 2-5 6h5v10z"/></svg></div>
<div class="abs qbadge" style="left:862px"><svg width="26" height="20" viewBox="0 0 26 20" fill="#3f8a1c"><path d="M0 20V11C0 4 4 0 10 0v4c-3 0-5 2-5 6h5v10zM14 20V11c0-7 4-11 10-11v4c-3 0-5 2-5 6h5v10z"/></svg></div>

<!-- quote -->
<div class="abs quote-bg" role="img" aria-label="Landscaper working among green foliage"></div>
<div class="abs quote-box"></div>
<h2 class="abs quote-title">REQUEST A<br>QUICK QUOTE</h2>
<div class="abs quote-photo" role="img" aria-label="Flower bed with pink hibiscus along a lawn"></div>
<div class="abs field f-first">First Name</div>
<div class="abs field f-email">Your Email</div>
<div class="abs field f-select">Snow Removal<svg width="10" height="6" viewBox="0 0 10 6" fill="none" stroke="#777" stroke-width="1.2"><path d="M1 1l4 4 4-4"/></svg></div>
<div class="abs field f-msg">Your message</div>
<div class="abs btn-black">SUBMIT NOW</div>

<!-- footer -->
<div class="abs foot-h" style="left:173px">ABOUT US</div>
<div class="abs foot-h" style="left:408px">OUR SERVICES</div>
<div class="abs foot-h" style="left:581px">QUICK LINKS</div>
<div class="abs foot-h" style="left:744px">CONTACT</div>
<div class="abs foot-h" style="left:910px">FOLLOW US</div>
<p class="abs foot-col foot-about" style="left:173px">Brookvale Yardworks strives to set the standard for the highest quality lawn and landscape products and services and to exceed our customer's expectations every time.</p>
<div class="abs foot-col foot-links" style="left:408px"><div>Turf Management</div><div>Hardscaping</div><div>Irrigation</div><div>Landscaping</div></div>
<div class="abs foot-col foot-links" style="left:581px"><div>About Us</div><div>Divisions</div><div>Certifications</div><div>Gallery</div></div>
<div class="abs foot-col" style="left:744px">BROOKVALE YARDWORKS<br>4120 W 62nd Terrace<br>Shawnee, KS 66200<br><br>Shawnee Office<br>1-913-555-0148<br>Junction City Office<br>1-785-555-0193</div>
<div class="abs social"><span></span><span></span><span></span></div>
<div class="abs foot-line"></div>
<div class="abs copy">Copyright 2021 Brookvale Yardworks. All Rights Reserved.</div>
<div class="abs legal">Terms of Use &nbsp;|&nbsp; Privacy Policy</div>

</body>
</html>
```